Software company seeks new website design

We are a UK based company called Meridian Loft. We build software which helps other businesses to manage their accounts and company finances. All of our clients enjoy full telephone based support as well as access to our software. So, we like to think that we are combining the best accountancy software in the world with a friendly human touch.
We need our homepage completely redesigned. At the moment we have two products which we want to highlight. They are called 'Quick Ledgerly' (which you can view at www.quickledgerly.example) and Tally Brook.
*VERY IMPORTANT!* We would like the focus of the site to be on our latest new product - Tally Brook.
We have included a variety of files to help you out, including graphics and some text. Our target audience is medium and large UK based companies who are interested in finding a cost effective and intelligent accountancy solution.
The main call to action on the home page should be EITHER 'learn more', 'find out more' or 'arrange a free demonstration'. If you are unsure about what the text should say then you can use 'Lorem Ipsum'.
Site that we like include:
http://vantorisoft.example/
http://www.plumegrid.example/
Thank you for viewing. We promise to give constructive feedback to every person who submits a design. Thank you so much. Good luck to you!
IMPORTANT UPDATE: THE ARTWORK HIVE WEBSITE KEEPS LOGGING ME OUT WHEN I TRY TO ADD FEEDBACK. I HAVE CONTACTED TECHNICAL SUPPORT AND I'M WAITING FOR A RESOLUTION. I SHALL OFFER FEEDBACK TO EVERY ONE OF YOU AS SOON AS THE ARTWORK HIVE WEBSITE IS WORKING PROPERLY
ANOTHER IMPORTANT UPDATE: I SAID ABOVE THAT I'D LIKE THE FOCUS ON THE SITE TO BE ON THE PRODUCT 'TALLY BROOK' - NOT QUICK LEDGERLY. ONE PERSON HAS ALREADY WASTED TIME BY NOT FOLLOWING THAT INSTRUCTION. SO, ONCE AGAIN - PLEASE MAKE THE FOCUS OF THE SITE ON TALLY BROOK - NOT QUICK LEDGERLY. THANKS FOLKS. I APPRECIATE YOU BEING HERE.
Reason: Sorry folks, there was a problem with the system which prevented me from leaving any feedback. That problem has now been resolved, however, the guy who is making the final decision is away for a few days. Thank you for everything so far. There's some really great designs so far. Every design will be checked out and given a comment. You have my word.
Reason: Sorry folks, it's been an incredibly busy week and we haven't had time to check the designs out.

```html
<!DOCTYPE html>
<html lang="en">
<head>
<meta charset="utf-8">
<title>Tally Brook by Meridian Loft – Home</title>
<link href="https://fonts.googleapis.com/css2?family=Source+Sans+3:wght@400;600&display=swap" rel="stylesheet">
<style>
:root{
  --brand:#5db6da;
  --brand-dark:#3d9fc6;
  --heading:#4aaed6;
  --partner:#4b3f93;
  --slider-band:#86b8cf;
  --text:#3f3f3f;
  --muted:#777;
  --rule:#cfcfcf;
  --white:#fff;
}
*{box-sizing:border-box;margin:0;padding:0}
html,body{width:1184px;height:1200px;overflow:hidden;background:var(--white)}
body{position:relative;font-family:"Source Sans 3",sans-serif;color:var(--text)}
.abs{position:absolute}

.site-header{left:0;top:0;width:1184px;height:55px}
.brand{left:217px;top:6px;display:flex;align-items:center;gap:8px}
.brand-mark{width:36px;height:36px;background:var(--brand)}
.brand-name{font-size:24px;font-weight:600;color:var(--brand-dark);line-height:1}
.brand-tag{font-size:8px;color:var(--brand-dark);margin-top:2px}
.call{right:213px;top:10px;font-size:14px;color:var(--muted)}
.call strong{font-size:24px;font-weight:600;color:var(--brand);letter-spacing:1px}

.main-nav{left:0;top:55px;width:1184px;height:55px;background:var(--brand)}
.main-nav ul{list-style:none;position:absolute;left:213px;width:757px;top:0;height:55px;display:flex;justify-content:space-between;align-items:center;padding:0 36px 0 44px}
.main-nav a{font-size:13px;font-weight:600;color:#2e6f8a;text-decoration:none}
.main-nav a.current{color:var(--white)}

.slider{left:213px;top:150px;width:757px;height:316px;background:var(--slider-band);border:2px solid #7fb3cc}
.slide{position:absolute;left:0;top:0;width:753px;height:266px;background:linear-gradient(180deg,#eef1f2 0%,#cfd3d4 55%,#8b8d8f 100%)}
.dots{position:absolute;left:0;right:0;top:287px;display:flex;justify-content:center;gap:5px}
.dots span{width:7px;height:7px;border-radius:50%;background:var(--white)}

.feature{top:502px;width:221px}
.feature h2{font-size:16.5px;font-weight:600;color:var(--heading);height:43px}
.feature .thumb{width:221px;height:78px}
.feature p{font-size:9.6px;line-height:17.5px;margin-top:14px;height:78px;padding-right:6px}
.btn{display:block;width:78px;height:27px;margin:0 auto;border-radius:2px;background:linear-gradient(#6fc2e3,#3d9fc6);color:var(--white);font-size:10px;text-align:center;line-height:27px;text-decoration:none}

.rule{left:213px;width:757px;height:1px;background:var(--rule)}

.unlock{left:211px;top:816px;font-size:18px;color:#444;display:flex;align-items:baseline;gap:10px;white-space:nowrap}
.partner{font-size:24px;font-weight:600;color:var(--partner);line-height:1}
.unlock-copy{left:634px;top:804px;width:340px;font-size:10.4px;line-height:14.5px;color:#555}

.intro{left:213px;top:918px;width:524px}
.intro h1{font-size:18px;font-weight:600;color:var(--heading)}
.intro h3{font-size:14px;font-weight:400;color:var(--heading);margin-top:8px}
.intro p{font-size:8.8px;line-height:15.8px;color:#555;margin-top:18px}
.intro p + p{margin-top:16px}

.promo{left:774px;width:196px;height:55px;border:1px solid #bdbdbd;display:flex;align-items:center;gap:8px;padding-left:10px}
.promo .icon{width:42px;height:40px;border-radius:3px;flex:none}
.promo span{font-size:10px;line-height:16px;color:#555;text-transform:uppercase}

.site-footer{left:0;top:1160px;width:1184px;height:40px;background:var(--brand)}
.site-footer small{position:absolute;left:213px;top:14px;font-size:9px;color:var(--white)}
.social{position:absolute;right:212px;top:9px;display:flex;gap:9px}
.social span{width:23px;height:23px;border-radius:50%;background:var(--white);border:2px solid #e4f2f8;opacity:.85}
</style>
</head>
<body>

<header class="site-header abs">
  <div class="brand abs">
    <div class="brand-mark"></div>
    <div>
      <div class="brand-name">Tally Brook</div>
      <div class="brand-tag">Unlock the potential of your accounts software</div>
    </div>
  </div>
  <div class="call abs">Call Now! <strong>0161 496 0382</strong></div>
</header>

<nav class="main-nav abs">
  <ul>
    <li><a class="current" href="#">Home</a></li>
    <li><a href="#">How it works</a></li>
    <li><a href="#">Services</a></li>
    <li><a href="#">Products</a></li>
    <li><a href="#">Partners</a></li>
    <li><a href="#">Contact</a></li>
  </ul>
</nav>

<section class="slider abs">
  <div class="slide" role="img" aria-label="Photo of a team of six smiling business people in suits"></div>
  <div class="dots"><span></span><span></span><span></span><span></span></div>
</section>

<article class="feature abs" style="left:213px">
  <h2>All reports you need...</h2>
  <div class="thumb" role="img" aria-label="Photo of a hand touching a blue digital interface" style="background:linear-gradient(90deg,#1d4d7a,#3c86b8,#1a3f66)"></div>
  <p>Lorem Ipsum has been the industry's standard dummy text ever since the 1500s, when an unknown printer took a galley of type and scrambled it to make a type specimen book.</p>
  <a class="btn" href="#">Learn More &gt;</a>
</article>

<article class="feature abs" style="left:481px">
  <h2>When you need them</h2>
  <div class="thumb" role="img" aria-label="Photo of colleagues working together at an office desk" style="background:linear-gradient(90deg,#cfd6dc,#8e9aa5,#dfe5ea)"></div>
  <p>When an unknown printer took a galley of type and scrambled it to make a type specimen book. It has survived not only five centuries, but also the leap into electronic .</p>
  <a class="btn" href="#">Learn More &gt;</a>
</article>

<article class="feature abs" style="left:750px">
  <h2>All the reports are formatted</h2>
  <div class="thumb" role="img" aria-label="Photo of hands joining white jigsaw puzzle pieces" style="background:linear-gradient(90deg,#3a2b28,#c9a99a 50%,#2c2220)"></div>
  <p>hen an unknown printer took a galley of type and scrambled it to make a type specimen book. It has survived not only five centuries not only five centuries.</p>
  <a class="btn" href="#">Learn More &gt;</a>
</article>

<div class="rule abs" style="top:773px"></div>

<div class="unlock abs">Unlock thepotential of your <span class="partner">Meridian Loft</span></div>
<p class="unlock-copy abs">Your Meridian Loft accounts system stores the most critical financial data in your organisation. TallyBrook is a service that gives you that information as meaningful, correctly formatted and timely reports, all at a fixed monthly price.</p>

<div class="rule abs" style="top:891px"></div>

<section class="intro abs">
  <h1>An innovative service that solves your reporting problems</h1>
  <h3>TallyBrook is a complete solution to the perennial problem of a lack of information</h3>
  <p>The lack of meaningful, timely and accurate information is &nbsp;an age-old problem. &nbsp;Many approaches have failed to solve this problem effectively. The use of GUI reporting or BI tools was meant to be a solution but, high failure rates and a massive gap between what was demonstrated and what was delivered has led to GUI reporting tools and BI tools taking pride of place in the “shelfware” category.</p>
  <p>The fault goes beyond tools that are difficult to use. Simply put, would you prefer to purchase the latest labour saving kitchen device or have a meal served to you on a plate? TallyBrook is exactly that - service on a plate. You order what you wish and we serve it you - online and in real time.</p>
</section>

<div class="promo abs" style="top:924px">
  <div class="icon" role="img" aria-label="Illustration of a pair of dice" style="background:linear-gradient(#f2f2f2,#bdbdbd)"></div>
  <span>Forecasting the future<br>just got easier</span>
</div>
<div class="promo abs" style="top:995px">
  <div class="icon" role="img" aria-label="Illustration of a hand holding a blue globe" style="background:linear-gradient(#4aa8e0,#d9a27a)"></div>
  <span>Keep your finger on the<br>pulse of your business</span>
</div>
<div class="promo abs" style="top:1066px">
  <div class="icon" role="img" aria-label="Illustration of a small house carried by figures" style="background:linear-gradient(#c9403a,#b5b5b5)"></div>
  <span>Building a business case<br>for report case</span>
</div>

<footer class="site-footer abs">
  <small>Copyright © 2012Tally Brook. All rights reserved.</small>
  <div class="social" aria-label="Social links"><span></span><span></span><span></span><span></span></div>
</footer>

</body>
</html>
```